Training Consultant for Oil and Gas Drillers needs logo for business cards

I teach oil and gas professionals the skills required to keep rigs from blowing up. The company name is "Night Shift Bore Safety", which is pronounced Nite Shiffed. Tour refers to the time on an oil rig when a worker is off for sleep and rest. I teach something called Well Control, which is how to maintain a pressure balance in the well so the hydro carbons don't come to surface unexpectedly( like the Grey Tide Platform).

Target Market(s)

Rig hands and oil companies

Contact Information for Business Card

Night Shift BS ( company name) with a new logo
My name (Derek Holloway )and Title (Well Control Consultant)
Phone number and address

Font styles to use
Serif
Sans Serif

Colors

Designer to choose colors to be used in the design.

Requirements
Must have
• I need a logo for the company. I do not have anything yet

```html
<!DOCTYPE html>
<html lang="en">
<head>
<meta charset="utf-8">
<title>Night Shift BS — Business Card</title>
<link rel="stylesheet" href="https://fonts.googleapis.com/css2?family=Cinzel:wght@500;600&family=Lato:wght@400;700&display=swap">
<style>
  :root {
    --page-bg: #e9ebee;
    --card-white: #fbfbfb;
    --blue-top: #0b8fd1;
    --blue-bottom: #0d4d9c;
    --accent-orange: #f0921e;
    --ink-dark: #2e2e2e;
    --text-light: #ffffff;
  }
  html, body {
    margin: 0;
    width: 1200px;
    height: 900px;
    overflow: hidden;
    background: var(--page-bg);
  }
  .business-card {
    position: absolute;
    left: 150px;
    top: 172px;
    width: 900px;
    height: 555px;
    background: var(--card-white);
    box-shadow: 0 10px 30px rgba(0,0,0,0.15);
    overflow: hidden;
    font-family: "Lato", sans-serif;
  }
  .card-panel {
    position: absolute;
    inset: 0;
    width: 100%;
    height: 100%;
  }
  .brand-mark {
    position: absolute;
    left: 143px;
    top: 176px;
    width: 140px;
    height: 140px;
    border-radius: 50%;
    background: var(--accent-orange);
  }
  .company-name {
    position: absolute;
    left: 20px;
    width: 380px;
    top: 418px;
    text-align: center;
    margin: 0;
    font-family: "Lato", sans-serif;
    font-weight: 700;
    font-size: 38px;
    line-height: 1.1;
    text-transform: uppercase;
    color: var(--ink-dark);
    white-space: nowrap;
  }
  .contact-block {
    position: absolute;
    right: 66px;
    top: 252px;
    text-align: right;
    color: var(--text-light);
  }
  .person-name {
    margin: 0;
    font-family: "Cinzel", serif;
    font-weight: 600;
    font-size: 33px;
    color: var(--accent-orange);
    letter-spacing: 1px;
    line-height: 1.1;
  }
  .person-title {
    margin: 6px 0 0;
    font-size: 24px;
    line-height: 1.2;
  }
  .contact-lines {
    margin: 20px 0 0;
    padding: 0;
    list-style: none;
    font-size: 24px;
    line-height: 34px;
  }
  .contact-lines li { display: flex; justify-content: flex-end; align-items: center; gap: 8px; }
  .contact-icon { width: 22px; height: 22px; flex: none; }
  .address-lines {
    margin: 14px 0 0;
    font-size: 24px;
    line-height: 33px;
    font-style: normal;
  }
</style>
</head>
<body>
  <div class="business-card">
    <svg class="card-panel" viewBox="0 0 652 402" preserveAspectRatio="none" aria-hidden="true">
      <defs>
        <linearGradient id="panelBlue" x1="0" y1="0" x2="0" y2="1">
          <stop offset="0" stop-color="var(--blue-top)"/>
          <stop offset="1" stop-color="var(--blue-bottom)"/>
        </linearGradient>
      </defs>
      <path d="M451,0 C462,40 440,110 372,160 C362,138 348,110 333,106 C318,104 300,170 291,230 C283,290 300,330 281,358 C330,362 385,388 432,402 L652,402 L652,0 Z"
            fill="url(#panelBlue)"/>
      <path d="M451,0 C462,40 440,110 372,160 C362,138 348,110 333,106 C318,104 300,170 291,230 C283,290 300,330 281,358 C330,362 385,388 432,402"
            fill="none" stroke="var(--accent-orange)" stroke-width="2.5"/>
    </svg>

    <div class="brand-mark" aria-hidden="true"></div>
    <p class="company-name">Night Shift BS</p>

    <div class="contact-block">
      <h1 class="person-name">DEREK HOLLOWAY</h1>
      <p class="person-title">Well Control Consultant</p>
      <ul class="contact-lines">
        <li>044-555 012 345
          <svg class="contact-icon" viewBox="0 0 24 24" aria-hidden="true"><path fill="var(--accent-orange)" d="M3 9c0-3 4-5 9-5s9 2 9 5l-3 2-3-2V8H9v1l-3 2-3-2zm4 3h10l2 7H5z"/></svg>
        </li>
        <li>hello@nightshiftbs.com
          <svg class="contact-icon" viewBox="0 0 24 24" aria-hidden="true"><rect x="3" y="6" width="18" height="13" fill="var(--accent-orange)"/><path d="M3 6l9 7 9-7" fill="none" stroke="var(--blue-bottom)" stroke-width="1.5"/></svg>
        </li>
      </ul>
      <address class="address-lines">421, Address line here<br>45452,Country Name</address>
    </div>
  </div>
</body>
</html>
```